I am a company selling interior designing materials

HI, I am selling interior design materials and require a namecard which is more outstanding while following a certain details placement as attached.

My clients are mainly interior designers so it has to attract their attention rather than feeling that its "just another namecard". I am selling wallcoverings, fabrics, acoustics and carpets.

Target Market(s)

interior designers designing hotels, commerical offices.

Contact Information for Business Card

As per attached.
Please change address to 47 Jalan 16 Tampines #05-02 Velmora Building Singapore 527314

Font styles to use
Other font styles liked:
• calibri

Requirements
Must have
• (1) company logo on top in the middle. Placement of contac details to be the same
• (2) company color is blue/green cymk 75/8/42/0
• (3) "KTV" logo to be prominent
• (4) You may change the logo but there should be a "swirl" surrounding the word KTV like current logo. The swirl pattern does not need to follow current logo and you may propose.
Should not have
• (1) there should not be any designs above "KTV" logo
• (2) no sharp triangles or angles

```html
<!DOCTYPE html>
<html lang="en">
<head>
<meta charset="utf-8">
<title>KTV Business Card</title>
<link href="https://fonts.googleapis.com/css2?family=Carlito:wght@400;700&display=swap" rel="stylesheet">
<style>
  :root {
    --teal: #1fa89b;
    --grey: #5b5b5b;
    --text: #4a4a4a;
    --paper: #f3f3f3;
    --white: #ffffff;
    --backdrop: #2e2e2e;
  }
  * { margin: 0; padding: 0; box-sizing: border-box; }
  html, body {
    width: 1200px; height: 960px; overflow: hidden;
    background: var(--backdrop);
    font-family: "Carlito", Calibri, sans-serif;
  }
  .stage { position: relative; width: 1200px; height: 960px; }
  .card {
    position: absolute; width: 600px; height: 342px;
    border-radius: 14px; overflow: hidden;
  }
  .card-front { left: 322px; top: 108px; background: var(--paper); }
  .card-back { left: 320px; top: 493px; background: var(--teal); }

  .brand-block {
    position: absolute; left: 40px; top: 128px; width: 250px; text-align: center;
  }
  .brand-mark {
    display: inline-flex; align-items: center; gap: 10px;
  }
  .brand-dot {
    width: 16px; height: 16px; border-radius: 50%; background: var(--teal);
  }
  .brand-name {
    font-weight: 700; font-size: 42px; line-height: 1; color: var(--grey); letter-spacing: 1px;
  }
  .company-name {
    margin-top: 14px; font-weight: 700; font-size: 13px; color: var(--grey); white-space: nowrap;
  }
  .divider {
    position: absolute; left: 309px; top: 92px; width: 2px; height: 158px;
    background: linear-gradient(to bottom, transparent, #9a9a9a 15%, #9a9a9a 85%, transparent);
  }
  .contact-block { position: absolute; left: 335px; top: 98px; color: var(--text); }
  .person-name {
    font-weight: 700; font-size: 21px; color: var(--teal); letter-spacing: 0.3px;
  }
  .address { margin-top: 10px; font-size: 15.5px; line-height: 19px; }
  .contact-list { list-style: none; margin-top: 7px; font-size: 15.5px; line-height: 19.5px; }
  .contact-list li { display: flex; align-items: center; gap: 8px; }
  .contact-list svg { width: 14px; height: 14px; flex: none; }
  .footer-band { position: absolute; left: 0; bottom: 0; width: 600px; height: 13px; }

  .back-brand {
    position: absolute; left: 0; top: 128px; width: 600px; text-align: center;
    font-weight: 700; font-size: 76px; line-height: 1; color: var(--white); letter-spacing: 2px;
  }
  .services {
    position: absolute; left: 0; top: 298px; width: 600px; text-align: center;
    font-weight: 700; font-size: 16px; color: var(--white);
  }
</style>
</head>
<body>
<main class="stage">
  <section class="card card-front">
    <div class="brand-block">
      <div class="brand-mark">
        <span class="brand-dot"></span>
        <span class="brand-name">KTV</span>
      </div>
      <p class="company-name">Kestrelvale Interior Furnishings Pte Ltd</p>
    </div>
    <div class="divider"></div>
    <div class="contact-block">
      <h1 class="person-name">LYDIA TAN</h1>
      <p class="address">47 Jalan 16 Tampines #05-02<br>Velmora Building Singapore 527314</p>
      <ul class="contact-list">
        <li>
          <svg viewBox="0 0 14 14"><rect x="3.5" y="0.5" width="7" height="13" rx="1.5" fill="none" stroke="var(--teal)" stroke-width="1.6"/><circle cx="7" cy="11" r="0.9" fill="var(--teal)"/></svg>
          (65) 9172 4406
        </li>
        <li>
          <svg viewBox="0 0 14 14"><rect x="1" y="3" width="12" height="8" rx="1" fill="var(--teal)"/><path d="M1.5 3.6 L7 7.6 L12.5 3.6" fill="none" stroke="var(--paper)" stroke-width="1"/></svg>
          lydia@ktvfurnishing.com
        </li>
        <li>
          <svg viewBox="0 0 14 14"><circle cx="7" cy="7" r="6" fill="var(--teal)"/><circle cx="5" cy="5.5" r="1.8" fill="var(--paper)"/><circle cx="9" cy="9.5" r="1.3" fill="var(--paper)"/></svg>
          www.ktvfurnishing.com
        </li>
      </ul>
    </div>
    <svg class="footer-band" viewBox="0 0 600 13" preserveAspectRatio="none">
      <polygon points="0,0 393,0 389,13 0,13" fill="var(--teal)"/>
      <polygon points="396,0 600,0 600,13 392,13" fill="var(--grey)"/>
    </svg>
  </section>

  <section class="card card-back">
    <p class="back-brand">KTV</p>
    <p class="services">Wallcoverings &nbsp;•&nbsp;Acoustic &nbsp;•&nbsp;Fabrics &nbsp;•&nbsp;Carpet</p>
  </section>
</main>
</body>
</html>
```